artist "stamp" design

Im a young artist. I`m making a stamp with my information so i can make homemade business cards, so I need the following information to look good together and simple to read:

Lorena Batalla Quiroga

www.lorebtqz.com

lorenabq47@fotmail.example

i want a very clan look, but with some personality. a simple logo or "look" would be great but nothing to fancy.

An idea I had was to make it look like it was written with a typewriter or a concept like that...be creative! thank you!
Updates

I don't want any image or icon, just letters, I need it to be compacto, I'm making a stamp

I don't want it to say photography 

I dont want my name to take over so it should stay close to the size as the rest of the info.

all my info should be included, this is not a logo its a design for a stamp meant to fin in a business card.

Target Market(s)

I'm a photographer, I want something very simple and I need this to make a stamp that ill use to pit on my cards and CV. I want something simple and modern

Industry/Entity Type

Business

Logo Text

Lorena Batalla Quiroga

Logo styles of interest
Abstract Logo
Wordmark Logo
Lettermark Logo
Font styles to use
Serif
Sans Serif

Requirements
Must have
• Has to look young and fresh
Nice to have
• Have to see how it looks on a business card with website and and email
Should not have
• Images

```html
<!DOCTYPE html>
<html lang="en">
<head>
<meta charset="utf-8">
<title>Lorena Batalla Quiroga — Stamp</title>
<link rel="stylesheet" href="https://fonts.googleapis.com/css2?family=Cutive&display=swap">
<style>
  :root {
    --ink: #1c1a1a;
    --paper: #ffffff;
  }
  html, body {
    margin: 0;
    padding: 0;
    width: 1200px;
    height: 1000px;
    overflow: hidden;
    background: var(--paper);
  }
  .stamp {
    position: relative;
    width: 1200px;
    height: 1000px;
    color: var(--ink);
    font-family: "Cutive", "Courier New", serif;
  }
  .stamp-frame {
    position: absolute;
    inset: 0;
  }
  .stamp-line {
    position: absolute;
    left: 0;
    width: 100%;
    margin: 0;
    text-align: center;
    white-space: nowrap;
    line-height: 1;
  }
  .name {
    font-size: 60px;
    letter-spacing: 0.14em;
  }
  .name .initial {
    font-size: 88px;
    letter-spacing: 0.04em;
  }
  .name-first { top: 278px; }
  .name-last  { top: 381px; }
  .contact {
    font-size: 56px;
    letter-spacing: 0.13em;
  }
  .website { top: 526px; }
  .email {
    top: 646px;
    font-size: 50px;
    letter-spacing: 0.06em;
  }
</style>
</head>
<body>
  <main class="stamp">
    <svg class="stamp-frame" width="1200" height="1000" viewBox="0 0 1200 1000" aria-hidden="true">
      <g fill="none" stroke="var(--ink)" stroke-width="5" stroke-linecap="butt">
        <path d="M76 219 L252 222" />
        <path d="M306 217 L1124 217" />
        <path d="M78 217 L79 782" />
        <path d="M1121 217 L1120 660" />
        <path d="M1121 695 L1122 782" />
        <path d="M76 779 L1124 779" />
      </g>
      <g stroke="var(--ink)" stroke-width="2">
        <path d="M110 775 L140 775" />
        <path d="M330 775 L350 775" />
        <path d="M620 775 L660 775" />
        <path d="M880 775 L900 775" />
        <path d="M1040 775 L1060 775" />
      </g>
    </svg>

    <p class="stamp-line name name-first"><span class="initial">L</span>orena <span class="initial">B</span>atalla</p>
    <p class="stamp-line name name-last"><span class="initial">Q</span>uiroga</p>
    <p class="stamp-line contact website">www.lorebtqz.com</p>
    <p class="stamp-line contact email">lorenabq47@fotmail.example</p>
  </main>
</body>
</html>
```